MCP phase 1 web design

Meridale Capital Partners Ltd (MCP) is a challenger business to the traditional leasing market. We look for solutions to complex problems involving the funding of capital equipment within an office environment and then build documentation around the solution. We recently created a brief for a logo and successfully completed that assignment. We now need to create our first web site which is simply intended to be informative. To help interested designers we have attached a detailed brief that is broken into three sections. The first explains how we see the site developing over time from something quite straightforward initially to a full transaction capability. Whoever wins this competition will be expected to work with us into the future to help develop the site. Section 2 gives you a view about our likes and dislikes by reviewing some existing sites. Section 3 gives you the structure and content of the site based upon our likes and dislikes. We are by no means committed to the structure and if you believe it can be presented in a better way then please use your design. The text is fixed as content. The images to appear can be anything from photographs to line drawings again entirely at the designers whim. Currently we have a home page plus 5 subsidiary pages. A few things to help you:
1. The logo is fixed and should be amongst the downloads.
2. The colours we have are corporate and should be used.
3. The typeface we use within the business is "Verdana"
Good luck.

Industry/Entity Type

Business

```html
<!DOCTYPE html>
<html lang="en">
<head>
<meta charset="utf-8">
<title>Meridale Capital Partners Ltd</title>
<link rel="stylesheet" href="https://fonts.googleapis.com/css2?family=Open+Sans:ital,wght@1,600&family=Oxygen:wght@400;700&display=swap">
<style>
:root{
  --blue:#1a6db3;
  --blue-dark:#135796;
  --blue-light:#9ccaf0;
  --ink:#4a4a4a;
  --ink-soft:#666;
  --line:#d4d4d4;
  --card:#fafafa;
  --btn-grey:#555;
  --foot:#ececec;
  --foot-bar:#dcdcdc;
}
*{box-sizing:border-box;margin:0;padding:0}
html,body{width:1200px;height:842px;overflow:hidden}
body{position:relative;background:#f7f7f7;font-family:"Oxygen",Verdana,sans-serif;color:var(--ink)}
.header{position:absolute;left:0;top:0;width:1200px;height:94px;background:linear-gradient(#ffffff,#ececec);border-bottom:1px solid #ddd}
.tagline{position:absolute;left:129px;top:19px;font-family:"Open Sans",Verdana,sans-serif;font-style:italic;font-weight:600;font-size:18.5px;line-height:23px;color:#666;letter-spacing:-.4px;text-transform:uppercase}
.hero{position:absolute;left:0;top:94px;width:1200px;height:393px;background:linear-gradient(170deg,#a9b3b1 0%,#6f7c79 35%,#37423f 60%,#8d9896 85%,#b9c1bf 100%)}
.brand-seal{position:absolute;left:529px;top:15px;width:142px;height:142px;border-radius:50%;background:linear-gradient(#f4f4f4,#d9d9d9);box-shadow:0 2px 6px rgba(0,0,0,.3);display:flex;align-items:center;justify-content:center;z-index:3}
.brand-seal span{display:flex;align-items:center;justify-content:center;width:124px;height:124px;border-radius:50%;background:linear-gradient(#fafafa,#e2e2e2);font-weight:700;font-size:36px;color:var(--blue);letter-spacing:1px}
.call{position:absolute;right:240px;top:20px;display:flex;align-items:center;gap:8px;font-size:16.5px;color:#666;white-space:nowrap;letter-spacing:-.2px}
.call b{color:#555;font-size:18px;margin-left:3px}
.menu-btn{position:absolute;left:972px;top:30px;width:75px;height:26px;border-radius:3px;background:linear-gradient(#2a83cc,var(--blue-dark));border:1px solid #0e4a80;color:#fff;font-size:13px;display:flex;align-items:center;justify-content:center;gap:4px;z-index:4}
.menu-panel{position:absolute;left:910px;top:67px;width:131px;height:108px;border-radius:5px;background:var(--blue-light);border:1px solid #7fb5e4;z-index:3}
.menu-panel a{position:absolute;left:8px;width:115px;height:25px;border-radius:3px;background:linear-gradient(#fafafa,#d4d4d4);border:1px solid #999;font-size:12.5px;color:#333;text-decoration:none;display:flex;align-items:center;justify-content:center}
.cards{position:absolute;left:0;top:352px}
.card{position:absolute;top:0;width:281px;height:343px;background:var(--card);border:1px solid var(--line);border-radius:3px;text-align:center}
.card::after{content:"";position:absolute;left:14px;right:14px;bottom:-10px;height:10px;background:radial-gradient(ellipse at top,rgba(0,0,0,.25),transparent 70%)}
.card-photo{position:absolute;left:9px;top:9px;width:263px;height:193px}
.card h2{position:absolute;left:0;right:0;top:210px;font-size:18px;font-weight:700;color:var(--blue);white-space:nowrap}
.card p{position:absolute;left:2px;right:2px;top:236px;font-size:12px;line-height:16px;color:#333;white-space:nowrap;letter-spacing:-.1px}
.btn{position:absolute;left:64px;top:293px;width:161px;height:38px;border-radius:2px;background:var(--blue);border:1px solid #0d4a80;color:#fff;font-size:16px;font-weight:700;display:flex;align-items:center;justify-content:center}
.btn.is-hover{background:var(--btn-grey);border-color:#333}
.footer{position:absolute;left:0;top:738px;width:1200px;height:74px;background:linear-gradient(#fafafa,var(--foot));border-top:1px solid var(--line)}
.foot-head{position:absolute;top:6px;display:flex;align-items:center;gap:6px;font-size:14px;font-weight:700;color:#555}
.divider{position:absolute;top:0;width:1px;height:74px;background:#ccc;box-shadow:1px 0 #fff}
.email{position:absolute;left:131px;top:34px;width:191px;height:30px;border:1px solid #ccc;background:#fff;border-radius:2px;font-size:13px;color:#888;padding:6px 7px}
.enter{position:absolute;left:334px;top:35px;width:65px;height:30px;border-radius:3px;background:var(--blue);border:1px solid #0d4a80;color:#fff;font-size:13px;font-weight:700;display:flex;align-items:center;justify-content:center}
.social{position:absolute;top:34px;width:30px;height:30px;border-radius:4px;background:var(--blue)}
.foot-brand{position:absolute;left:757px;top:13px;height:52px;display:flex;align-items:center;gap:12px;color:var(--blue);font-weight:700}
.foot-brand .mark{font-size:34px}
.foot-brand .rule{width:1px;height:50px;background:#999}
.foot-brand .name{font-size:17px;line-height:20px;letter-spacing:.5px}
.bottom-bar{position:absolute;left:0;top:812px;width:1200px;height:30px;background:var(--foot-bar);border-top:1px solid #c8c8c8;font-size:13px;color:#333}
.bottom-bar .copy{position:absolute;left:131px;top:6px}
.bottom-bar .legal{position:absolute;right:131px;top:6px}
</style>
</head>
<body>
<header class="header">
  <p class="tagline">We are a challenger business to<br>the traditional leasing market</p>
  <div class="call">
    <svg width="27" height="27" viewBox="0 0 24 24"><path fill="#1a6db3" d="M6.6 10.8a15.5 15.5 0 0 0 6.6 6.6l2.2-2.2c.3-.3.7-.4 1-.2 1.1.4 2.3.6 3.6.6.6 0 1 .4 1 1V20c0 .6-.4 1-1 1A17 17 0 0 1 3 4c0-.6.4-1 1-1h3.5c.6 0 1 .4 1 1 0 1.3.2 2.5.6 3.6.1.3 0 .7-.2 1z"/></svg>
    <span>CALL US ON:<b>020 7946 0321</b></span>
  </div>
  <div class="menu-btn">
    <svg width="11" height="12" viewBox="0 0 11 12"><rect x="1" y="1" width="9" height="10" fill="none" stroke="#fff" stroke-width="1.3"/><path d="M3 4h5M3 6h5M3 8h5" stroke="#fff"/></svg>
    MENU
    <svg width="8" height="5" viewBox="0 0 8 5"><path d="M0 0h8L4 5z" fill="#fff"/></svg>
  </div>
</header>

<div class="brand-seal"><span>MCP</span></div>

<nav class="menu-panel">
  <a href="#" style="top:9px">Why Alternative ?</a>
  <a href="#" style="top:41px">Solutions</a>
  <a href="#" style="top:73px">Contact Us</a>
</nav>

<div class="hero" role="img" aria-label="Rowing crew in a long boat cutting across rippling river water"></div>

<section class="cards">
  <article class="card" style="left:132px">
    <div class="card-photo" role="img" aria-label="Glowing globe of coloured image tiles on black" style="background:radial-gradient(circle at 50% 48%,#b08aa8 0%,#6f6f88 28%,#1c1c22 45%,#000 70%)"></div>
    <h2>Managed Services Solutions</h2>
    <p>Lorem ipsum dolor sit amet, consectetuer adipis<br>cing elit, sed diamnonummy nibh euismod tin-<br>cidunt ut laoreet</p>
    <div class="btn">READ MORE</div>
  </article>
  <article class="card" style="left:459px">
    <div class="card-photo" role="img" aria-label="Office staff seated at a desk with computers and paperwork" style="background:linear-gradient(135deg,#e4e8ec 0%,#c9ced3 45%,#4b4d52 75%,#d9d5cf 100%)"></div>
    <h2>Public Sector Solutions</h2>
    <p>Lorem ipsum dolor sit amet, consectetuer adipis<br>cing elit, sed diamnonummy nibh euismod tin-<br>cidunt ut laoreet</p>
    <div class="btn">READ MORE</div>
  </article>
  <article class="card" style="left:787px">
    <div class="card-photo" role="img" aria-label="Students seated in a lecture room with open books" style="background:linear-gradient(150deg,#b8b2b8 0%,#8a7f88 35%,#d9a888 60%,#3f4a5e 100%)"></div>
    <h2>Education Solutions</h2>
    <p>Lorem ipsum dolor sit amet, consectetuer adipis<br>cing elit, sed diamnonummy nibh euismod tin-<br>cidunt ut laoreet</p>
    <div class="btn is-hover">READ MORE</div>
  </article>
</section>

<footer class="footer">
  <div class="foot-head" style="left:131px">
    <svg width="21" height="14" viewBox="0 0 21 14"><rect x=".5" y=".5" width="20" height="13" fill="#1a6db3"/><path d="M1 1l9.5 7L20 1" fill="none" stroke="#fff" stroke-width="1.3"/></svg>
    NEWSLETTER
  </div>
  <div class="email">your email address</div>
  <div class="enter">ENTER</div>
  <div class="divider" style="left:455px"></div>
  <div class="foot-head" style="left:513px">
    <svg width="23" height="19" viewBox="0 0 23 19"><ellipse cx="9" cy="8" rx="8" ry="6.5" fill="none" stroke="#1a6db3" stroke-width="1.8"/><path d="M4 13l-2 4 5-2.5" fill="#1a6db3"/></svg>
    SOCIAL MEDIA
  </div>
  <div class="social" style="left:512px"></div>
  <div class="social" style="left:551px"></div>
  <div class="social" style="left:591px"></div>
  <div class="divider" style="left:698px"></div>
  <div class="foot-brand">
    <span class="mark">MCP</span>
    <span class="rule"></span>
    <span class="name">MERIDALE CAPITAL<br>PARTNERS LTD</span>
  </div>
</footer>
<div class="bottom-bar">
  <span class="copy">© 2014 Meridalecp. All Rights Reserved.</span>
  <span class="legal">Terms and conditions | Privacy Policy</span>
</div>
</body>
</html>
```